Business card design needed

I am a small start up business in the mortgage broking industry based in Sydney called 'keys2nest'. I will be providing residential mortgages to first home owners, investors and people looking to refinance. I would like to see designs that use the colors blue, black, and white - same as my logo (see logo design uploaded)

Target Market(s)

My target market is First Home Owners, property investors, and people looking to refinance. The loans I will be providing are for residential property only at this stage, and my clients will predominantly be in the 30-50yr age bracket.

Industry/Entity Type

Residential

Contact Information for Business Card

Owen Partridge
Director/Mobile Mortgage Broker
keys2nest
PO BOX 4287
Westmead NSW 2145
Mb: 0491 862 307
email: owen@keys2nest.com.au

Requirements
Must have
• please use lower case for business name (i.e. keys2nest)

```html
<!DOCTYPE html>
<html lang="en">
<head>
<meta charset="utf-8">
<title>keys2nest – Business Card</title>
<link rel="stylesheet" href="https://fonts.googleapis.com/css2?family=Aldrich&display=swap">
<style>
  :root {
    --card-bg: #000000;
    --ink: #ffffff;
    --accent: #4fc8ec;
    --type: "Aldrich", sans-serif;
  }
  * { margin: 0; padding: 0; box-sizing: border-box; }
  html, body {
    width: 1200px;
    height: 741px;
    overflow: hidden;
    background: var(--card-bg);
  }
  .card {
    position: relative;
    width: 1200px;
    height: 741px;
    background: var(--card-bg);
    color: var(--ink);
    font-family: var(--type);
  }
  .brand-name {
    position: absolute;
    left: 255px;
    width: 689px;
    top: 262px;
    text-align: center;
    font-size: 82px;
    line-height: 1;
    letter-spacing: 1px;
    text-transform: lowercase;
    color: var(--ink);
  }
  .brand-rule {
    position: absolute;
    left: 255px;
    top: 349px;
    width: 689px;
    height: 2px;
    background: var(--accent);
  }
  .contact {
    position: absolute;
    left: 356px;
    top: 358px;
  }
  .contact-name {
    font-size: 50px;
    line-height: 56px;
    letter-spacing: 2px;
    font-weight: 400;
  }
  .contact-details {
    list-style: none;
    font-size: 26px;
    line-height: 27px;
    letter-spacing: 1px;
  }
</style>
</head>
<body>
  <main class="card">
    <div class="brand-name">keys2nest</div>
    <div class="brand-rule"></div>
    <section class="contact">
      <h1 class="contact-name">Owen Partridge</h1>
      <ul class="contact-details">
        <li class="contact-role">Director/Mobile Mortgage Broker</li>
        <li class="contact-address">PO BOX 4287 Westmead NSW 2145</li>
        <li class="contact-phone">Mb: 0491 862 307</li>
        <li class="contact-email">email: owen@keys2nest.com.au</li>
      </ul>
    </section>
  </main>
</body>
</html>
```